Stationery Design Project

Brisk-Span Consultants is interim management company. We are specialized in finding the best Finance and IT consultants for our clients when they require additional resources on an interim basis for projects or special situations. We are flexible in our approach and we always seek to maximize the benefits for our clients as well as our consultants.

We are looking for a design of our letterhead, general stationery and business cards using the company name. The design will also be found on our coming web pages.
Updates

Please also create a logo for Brisk-Span Consultants which expresses that we want to match the best finance and IT people to our customers projects

Target Market(s)

Larger and mid sized companies (all sectors), as well as highly skilled Finance & IT professionals/consultants

Industry/Entity Type

Business

Requirements
Must have
• Brisk-Span Consultants
We are expecting that 'Brisk-Span' will be on the first line and 'Consultants' on a second line.
Please also indicate style of the letters for our address/phone and mail details. Our current address is:
Tornagervej 14,
2915 Skovlunde
Danmark
Mobile: +45 XX XX XX XX Mail: xx@brisk-span.dk

```html
<!DOCTYPE html>
<html lang="en">
<head>
<meta charset="utf-8">
<title>Brisk-Span Consultants – Stationery</title>
<link rel="stylesheet" href="https://fonts.googleapis.com/css2?family=Arimo:wght@400;700&display=swap">
<style>
  :root {
    --backdrop: #2e2e2e;
    --paper: #ffffff;
    --envelope: #e6e6e6;
    --ink: #1a1a1a;
    --brand-grey: #3d3d3d;
    --brand-navy: #1d2a8c;
    --navy-deep: #151d6b;
    --navy-light: #2f3db0;
    --mark-grey: #b5adb0;
    --band-grey: #3a3a3a;
  }
  * { box-sizing: border-box; margin: 0; padding: 0; }
  html, body { width: 1200px; height: 1032px; overflow: hidden; }
  body {
    background: var(--backdrop);
    font-family: "Arimo", Arial, sans-serif;
    color: var(--ink);
    position: relative;
  }
  .sheet { position: absolute; overflow: hidden; }

  /* brand lockup */
  .brand { position: absolute; display: flex; align-items: center; gap: 8px; }
  .brand-dot { border-radius: 50%; background: var(--brand-navy); flex: none; }
  .brand-name {
    font-weight: 700; color: var(--brand-grey); line-height: 1;
    text-transform: uppercase; white-space: nowrap;
  }
  .brand-name .line-two { display: block; letter-spacing: 0.32em; }

  .address { position: absolute; font-size: 13px; line-height: 15px; font-style: normal; white-space: nowrap; }
  .corner-disc { position: absolute; border-radius: 50%; background: var(--mark-grey); }
  .footer-band { position: absolute; left: 0; bottom: 0; width: 100%; display: block; }

  /* letterhead */
  .letterhead { left: 142px; top: 24px; width: 689px; height: 970px; background: var(--paper); }
  .letterhead .corner-disc { left: 71px; top: 87px; width: 80px; height: 80px; }
  .letterhead .brand { left: 447px; top: 822px; }
  .letterhead .brand-dot { width: 42px; height: 42px; }
  .letterhead .brand-name { font-size: 24px; }
  .letterhead .brand-name .line-two { font-size: 10px; margin-top: 3px; }
  .letterhead .address { left: 501px; top: 872px; }
  .letterhead .footer-band { height: 14px; }

  /* envelope */
  .envelope { left: 381px; top: 88px; width: 622px; height: 433px; background: var(--envelope); }
  .envelope .corner-disc { left: 30px; top: 28px; width: 70px; height: 70px; }
  .recipient-line { position: absolute; left: 132px; width: 210px; border-top: 1.5px solid var(--ink); }
  .envelope .brand { left: 402px; top: 292px; }
  .envelope .brand-dot { width: 38px; height: 38px; }
  .envelope .brand-name { font-size: 22px; }
  .envelope .brand-name .line-two { font-size: 9px; margin-top: 3px; }
  .envelope .address { left: 447px; top: 338px; font-size: 12px; line-height: 14px; }
  .envelope .footer-band { height: 14px; }

  /* business card, back */
  .card-back {
    left: 875px; top: 535px; width: 305px; height: 190px;
    background: linear-gradient(135deg, var(--navy-light), var(--navy-deep));
  }
  .card-back .brand { left: 0; right: 0; top: 70px; justify-content: center; }
  .card-back .brand-name { color: var(--paper); font-size: 30px; text-align: left; }
  .card-back .brand-name .line-two { font-size: 12px; margin-top: 4px; letter-spacing: 0.42em; }

  /* business card, front */
  .card-front { left: 560px; top: 554px; width: 327px; height: 213px; background: var(--paper); }
  .card-front .brand { left: 40px; top: 20px; gap: 6px; }
  .card-front .brand-dot { width: 24px; height: 24px; }
  .card-front .brand-name { font-size: 14px; }
  .card-front .brand-name .line-two { font-size: 6px; margin-top: 2px; }
  .card-holder { position: absolute; left: 207px; top: 60px; font-size: 10.5px; line-height: 13px; text-transform: uppercase; }
  .card-front .address { left: 192px; top: 132px; font-size: 10px; line-height: 12px; }
  .card-front .footer-band { height: 10px; }
</style>
</head>
<body>

  <section class="sheet letterhead" aria-label="Letterhead">
    <div class="corner-disc"></div>
    <div class="brand">
      <span class="brand-dot"></span>
      <span class="brand-name">Brisk-Span<span class="line-two">Consultants</span></span>
    </div>
    <address class="address">
      Tornagervej 14<br>2915 Skovlunde<br>Danmark<br>Mobile: +45 XX XX XX XX<br>Mail: XX@brisk-span.dk
    </address>
    <svg class="footer-band" viewBox="0 0 689 14" preserveAspectRatio="none">
      <polygon points="0,0 280,0 270,14 0,14" fill="var(--band-grey)"/>
      <polygon points="290,0 689,0 689,14 280,14" fill="var(--brand-navy)"/>
    </svg>
  </section>

  <section class="sheet envelope" aria-label="Envelope">
    <div class="corner-disc"></div>
    <div class="recipient-line" style="top:136px"></div>
    <div class="recipient-line" style="top:173px"></div>
    <div class="brand">
      <span class="brand-dot"></span>
      <span class="brand-name">Brisk-Span<span class="line-two">Consultants</span></span>
    </div>
    <address class="address">
      Tornagervej 14<br>2915 Skovlunde<br>Danmark<br>Mobile: +45 XX XX XX XX<br>Mail: XX@brisk-span.dk
    </address>
    <svg class="footer-band" viewBox="0 0 622 14" preserveAspectRatio="none">
      <polygon points="0,0 372,0 362,14 0,14" fill="var(--band-grey)"/>
      <polygon points="382,0 622,0 622,14 372,14" fill="var(--brand-navy)"/>
    </svg>
  </section>

  <section class="sheet card-back" aria-label="Business card, back">
    <div class="brand">
      <span class="brand-name">Brisk-Span<span class="line-two">Consultants</span></span>
    </div>
  </section>

  <section class="sheet card-front" aria-label="Business card, front">
    <div class="brand">
      <span class="brand-dot"></span>
      <span class="brand-name">Brisk-Span<span class="line-two">Consultants</span></span>
    </div>
    <div class="card-holder">Name<br>Designation</div>
    <address class="address">
      Tornagervej 14<br>2915 Skovlunde<br>Danmark<br>Mobile: +45 XX XX XX XX<br>Mail: XX@brisk-span.dk
    </address>
    <svg class="footer-band" viewBox="0 0 327 10" preserveAspectRatio="none">
      <polygon points="0,0 192,0 185,10 0,10" fill="var(--band-grey)"/>
      <polygon points="199,0 327,0 327,10 192,10" fill="var(--brand-navy)"/>
    </svg>
  </section>

</body>
</html>
```